Consulting company, design, Interior design in commercial real estate (Tertiai sector *

Company name: VORANDEL: from the Greek Evexia well-being, was born from a desire to combine well-being and work. By the choice of design, materials, design and furniture, everything is thought from this perspective

Logo: Essay with Möbius Ribbon and / or with the infinite acronym / and or triangle ...
Sentences to write:
"The exclusive partner for your development projects"
"Consulting - Design - Construction"
"We manage EVERYTHING for you"

On the back: Photo (attached; if photo is not clear, another photo can be provided) with company name and "VORANDEL, Excellence and reliability"
My name / First name: provided later (double name), Manager
Address: supplied later
Tel: supplied later
Website: www. vorandel.com
Colors: Black, gold and white. Other admissible colors
See attached files

Real estate business

Nom de l'entreprise : VORANDEL : du grec Evexia bien être, est né d'une volonté de faire rimer bien être et travail. Par le choix de la conception, des matériaux, du design et du mobilier, tout est pensé dans cette optique

Logo : Essai avec Ruban de Möbius et /ou avec le sigle infini / et ou triangle...
Phrases à inscrire :
"Le partenaire exclusif de vos projets d'aménagement"
"Conseil - Conception - Construction"
"Nous gérons TOUT pour vous"

Au verso : Photo (ci-jointe ; si photo pas nette, une autre photo peut être fournie) avec nom de l'entreprise et Mention "VORANDEL, Excellence et fiabilité"
Mon nom / Prénom : fourni ultérieurement (prénom double), Gérant
Adresse : fourni ultérieurement
Tél : fourni ultérieurement
Site Web : www. vorandel.com
Couleurs : Noir, doré et blanc. Autre couleurs recevables
Voir fichiers ci-joint

• My project must be simple, clear, neat and design.
The business card must catch the customer

```html
<!DOCTYPE html>
<html lang="fr">
<head>
<meta charset="utf-8">
<title>Vorandel – cartes de visite</title>
<link rel="stylesheet" href="https://fonts.googleapis.com/css2?family=Montserrat:wght@300;400;500;600;700&display=swap">
<style>
  :root{
    --stage:#1e1e22;
    --ink:#0b0b0c;
    --paper:#ffffff;
    --gold:#c9a43a;
    --gold-light:#ecd27a;
    --gold-deep:#9c7a1f;
    --text-dark:#1a1a1a;
    --text-light:#f4f4f4;
  }
  *{box-sizing:border-box;margin:0;padding:0}
  html,body{width:1200px;height:800px;overflow:hidden;background:var(--stage)}
  .stage{position:relative;width:1200px;height:800px;display:flex;align-items:center;justify-content:center;gap:44px}
  .card{position:relative;width:540px;height:310px;border-radius:18px;overflow:hidden;box-shadow:0 12px 30px rgba(0,0,0,.45);font-family:'Montserrat',sans-serif}

  /* back */
  .card-back{background:var(--ink);color:var(--text-light)}
  .card-back .art{position:absolute;inset:0}
  .back-info{position:absolute;left:300px;top:30px;right:22px}
  .brand-name{font-family:'Montserrat',sans-serif;font-weight:600;letter-spacing:.08em;line-height:1}
  .back-info .brand-name{color:var(--gold);font-size:26px}
  .person{margin-top:34px;font-size:13px;letter-spacing:.02em;line-height:1.2}
  .person strong{font-weight:700}
  .role{color:var(--gold);font-size:12px;text-align:right;margin-top:3px}
  .contact{margin-top:24px;font-size:11.5px;line-height:1.65;font-weight:400}
  .contact-row{display:flex;align-items:center;gap:8px}
  .contact-row svg{flex:none}

  /* front */
  .card-front{background:var(--paper);color:var(--text-dark)}
  .gold-edge{position:absolute;left:0;right:0;bottom:0;height:7px;background:linear-gradient(90deg,var(--gold-deep),var(--gold-light),var(--gold))}
  .logo-block{position:absolute;left:30px;top:96px;width:230px;display:flex;flex-direction:column;align-items:center}
  .logo-dot{width:54px;height:54px;border-radius:50%;background:var(--gold);margin-bottom:16px}
  .logo-block .brand-name{color:var(--text-dark);font-size:28px}
  .pitch{position:absolute;left:280px;top:34px;right:28px}
  .headline{font-size:19px;font-weight:400;letter-spacing:.06em;line-height:1.15}
  .headline strong{font-weight:700}
  .rule{height:1px;background:var(--gold);margin:12px 0}
  .services{font-size:11.5px;letter-spacing:.14em;line-height:1.35;font-weight:400}
  .partner{font-size:11.5px;font-weight:700;letter-spacing:.02em;line-height:1.4;text-transform:uppercase}
  .web-line{position:absolute;left:28px;right:28px;bottom:40px;height:1px;background:var(--gold)}
  .web{position:absolute;left:0;right:0;bottom:16px;text-align:center;font-size:12px;font-weight:500;letter-spacing:.55em}
</style>
</head>
<body>
<main class="stage">

  <article class="card card-back" aria-label="Verso de la carte">
    <svg class="art" width="540" height="310" viewBox="0 0 540 310">
      <defs>
        <linearGradient id="goldArc" x1="0" y1="0" x2="0" y2="1">
          <stop offset="0" stop-color="#ecd27a"/>
          <stop offset=".5" stop-color="#c9a43a"/>
          <stop offset="1" stop-color="#9c7a1f"/>
        </linearGradient>
        <linearGradient id="photoTone" x1="0" y1="0" x2="1" y2="1">
          <stop offset="0" stop-color="#ece9df"/>
          <stop offset=".55" stop-color="#b9a99a"/>
          <stop offset="1" stop-color="#2b3347"/>
        </linearGradient>
      </defs>
      <circle cx="110" cy="170" r="190" fill="url(#goldArc)"/>
      <circle cx="98" cy="170" r="188" fill="url(#photoTone)" role="img" aria-label="Portrait photo du gérant"/>
    </svg>
    <div class="back-info">
      <div class="brand-name">VORANDEL</div>
      <div class="person"><strong>MARC-ANTOINE</strong> DELVAUX</div>
      <div class="role">Gérant</div>
      <div class="contact">
        <div>14 Allée des Tilleuls</div>
        <div>01250 St MARTIN DES BOIS</div>
        <div class="contact-row">06 12 47 39 05
          <svg width="14" height="14" viewBox="0 0 14 14"><circle cx="7" cy="7" r="7" fill="var(--gold)"/><path d="M4.5 3.8l1.4-.3.7 1.7-.8.7a5 5 0 0 0 2.3 2.3l.7-.8 1.7.7-.3 1.4c-3 .2-5.9-2.7-5.7-5.7z" fill="var(--ink)"/></svg>
        </div>
        <div class="contact-row">www.vorandel.com
          <svg width="14" height="14" viewBox="0 0 14 14"><circle cx="7" cy="7" r="7" fill="var(--gold)"/><g fill="none" stroke="var(--ink)" stroke-width=".9"><circle cx="7" cy="7" r="4"/><ellipse cx="7" cy="7" rx="1.8" ry="4"/><path d="M3 7h8"/></g></svg>
        </div>
      </div>
    </div>
  </article>

  <article class="card card-front" aria-label="Recto de la carte">
    <div class="logo-block">
      <div class="logo-dot"></div>
      <div class="brand-name">VORANDEL</div>
    </div>
    <div class="pitch">
      <p class="headline">NOUS GÉRONS <strong>TOUT</strong><br>POUR VOUS</p>
      <div class="rule"></div>
      <p class="services">CONSEIL<br>CONCEPTION<br>CONSTRUCTION</p>
      <div class="rule"></div>
      <p class="partner">Le partenaire exclusif<br>de vos<br>projets d'aménagement</p>
    </div>
    <div class="web-line"></div>
    <p class="web">WWW.VORANDEL.COM</p>
    <div class="gold-edge"></div>
  </article>

</main>
</body>
</html>
```